Bref créative |
Birch Hydraulic | ||
Use same font as used in my logo | ||
Cutting-Edge Corporate Professional Simple |
Paul Destry | ||
Owner | ||
4637 Heron Ridge Lane Clarkston MI 48351 |
destry.paul@mailvane.net | ||

```html
<!DOCTYPE html>
<html lang="en">
<head>
<meta charset="utf-8">
<title>Birch Hydraulic — Stationery Set</title>
<link href="https://fonts.googleapis.com/css2?family=Source+Sans+3:wght@400;600;700&display=swap" rel="stylesheet">
<style>
  :root {
    --green: #1f9a3a;
    --green-deep: #0f7a2a;
    --green-light: #8fd06a;
    --leaf: #a9dc7a;
    --ink: #222;
    --paper: #ffffff;
    --stage: #ffffff;
    --edge: #1f9a3a;
  }
  html, body {
    margin: 0;
    width: 1200px;
    height: 881px;
    overflow: hidden;
    background: var(--stage);
    font-family: "Source Sans 3", "Myriad Pro", sans-serif;
  }
  .canvas { position: relative; width: 1200px; height: 881px; }
  .piece {
    position: absolute;
    background: var(--paper);
    border: 1px solid var(--edge);
    overflow: hidden;
  }
  .piece svg.art { position: absolute; inset: 0; width: 100%; height: 100%; }
  .brand {
    position: absolute;
    display: flex;
    align-items: center;
    gap: 8px;
    color: var(--green-deep);
    font-weight: 700;
    font-size: 22px;
    line-height: 1;
    z-index: 1;
  }
  .brand-mark { width: 14px; height: 14px; background: var(--green-deep); }
  .address {
    position: absolute;
    margin: 0;
    color: var(--green);
    font-size: 13px;
    line-height: 1.45;
    z-index: 1;
  }
  .contact {
    position: absolute;
    margin: 0;
    display: grid;
    grid-template-columns: 62px auto;
    font-size: 11px;
    line-height: 1.4;
    z-index: 1;
  }
  .contact dt { font-weight: 700; }
  .contact dd { margin: 0; }
  .contact.on-green { color: #fff; }
  .contact.on-paper { color: var(--ink); }
  .leaves { position: absolute; }

  /* Letterhead */
  .letterhead { left: 7px; top: 7px; width: 672px; height: 868px; }
  .letterhead .brand { left: 40px; top: 70px; }
  .letterhead .address { left: 50px; top: 168px; }
  .letterhead .contact { left: 462px; top: 802px; }

  /* Business card */
  .card { left: 696px; top: 5px; width: 496px; height: 278px; }
  .card .brand { left: 138px; top: 48px; font-size: 20px; }
  .card .holder { position: absolute; left: 340px; top: 82px; }
  .card .holder-name { margin: 0; color: var(--green); font-weight: 700; font-size: 18px; }
  .card .holder-role { margin: 0; color: var(--ink); font-size: 14px; }
  .card .address { left: 140px; top: 160px; font-size: 12px; }
  .card .contact { left: 140px; top: 208px; }

  /* Envelope */
  .envelope { left: 461px; top: 319px; width: 733px; height: 396px; }
  .envelope .brand { left: 10px; top: 104px; }
  .envelope .address { left: 18px; top: 150px; }
  .envelope .contact { left: 520px; top: 322px; }
</style>
</head>
<body>
<main class="canvas">

  <section class="piece letterhead" aria-label="Letterhead">
    <svg class="art" viewBox="0 0 672 868" preserveAspectRatio="none" aria-hidden="true">
      <defs>
        <linearGradient id="lh-band" x1="0" y1="0" x2="1" y2="0">
          <stop offset="0" stop-color="#0f7a2a"/><stop offset="1" stop-color="#35b24a"/>
        </linearGradient>
      </defs>
      <path d="M0 735 C180 700 330 770 672 680 L672 868 L0 868 Z" fill="url(#lh-band)"/>
      <path d="M0 760 C200 720 360 820 672 730 L672 868 L0 868 Z" fill="#fff" opacity="0.15"/>
      <path d="M0 800 C220 760 420 800 672 775" stroke="#fff" stroke-width="3" fill="none" opacity="0.6"/>
    </svg>
    <div class="leaves" role="img" aria-label="Faint leaf sprig decoration" style="left:90px;top:690px;width:110px;height:70px;border-radius:50%;background:radial-gradient(ellipse,rgba(169,220,122,.55),rgba(169,220,122,0) 70%);"></div>
    <div class="brand"><span class="brand-mark"></span>Birch Hydraulic</div>
    <p class="address">4637 Heron Ridge Lane<br>Clarkston MI 48351</p>
    <dl class="contact on-green">
      <dt>Phone</dt><dd>586-555-0140</dd>
      <dt>Cell</dt><dd>586-555-0172</dd>
      <dt>Fax</dt><dd>586-555-0143</dd>
      <dt>Email</dt><dd>destry.paul@mailvane.net</dd>
    </dl>
  </section>

  <section class="piece card" aria-label="Business card">
    <svg class="art" viewBox="0 0 496 278" preserveAspectRatio="none" aria-hidden="true">
      <defs>
        <linearGradient id="card-band" x1="0" y1="0" x2="0" y2="1">
          <stop offset="0" stop-color="#35b24a"/><stop offset="1" stop-color="#0f7a2a"/>
        </linearGradient>
      </defs>
      <path d="M0 0 L80 0 C30 60 40 170 130 278 L0 278 Z" fill="url(#card-band)"/>
      <path d="M80 0 C40 70 60 180 140 278" stroke="#8fd06a" stroke-width="3" fill="none"/>
    </svg>
    <div class="leaves" role="img" aria-label="Leaf sprig decoration" style="left:50px;top:130px;width:60px;height:80px;border-radius:50%;background:radial-gradient(ellipse,rgba(169,220,122,.9),rgba(169,220,122,0) 70%);"></div>
    <div class="brand"><span class="brand-mark"></span>Birch Hydraulic</div>
    <div class="holder">
      <p class="holder-name">Paul Destry</p>
      <p class="holder-role">Owner</p>
    </div>
    <p class="address">4637 Heron Ridge Lane<br>Clarkston MI 48351</p>
    <dl class="contact on-paper">
      <dt>Phone</dt><dd>586-555-0140</dd>
      <dt>Cell</dt><dd>586-555-0172</dd>
      <dt>Fax</dt><dd>586-555-0143</dd>
      <dt>Email</dt><dd>destry.paul@mailvane.net</dd>
    </dl>
  </section>

  <section class="piece envelope" aria-label="Envelope">
    <svg class="art" viewBox="0 0 733 396" preserveAspectRatio="none" aria-hidden="true">
      <defs>
        <linearGradient id="env-flap" x1="0" y1="0" x2="1" y2="0">
          <stop offset="0" stop-color="#0f7a2a"/><stop offset="1" stop-color="#3cb84e"/>
        </linearGradient>
        <linearGradient id="env-band" x1="0" y1="0" x2="1" y2="0">
          <stop offset="0" stop-color="#3cb84e"/><stop offset="1" stop-color="#0f7a2a"/>
        </linearGradient>
      </defs>
      <path d="M0 0 L733 0 L733 40 C500 100 250 55 0 80 Z" fill="url(#env-flap)"/>
      <path d="M0 80 C250 55 500 100 733 40" stroke="#8fd06a" stroke-width="3" fill="none"/>
      <path d="M0 320 C200 290 380 330 520 300 C620 280 690 240 733 200 L733 396 L0 396 Z" fill="url(#env-band)"/>
      <path d="M0 345 C220 310 420 350 733 250" stroke="#fff" stroke-width="3" fill="none" opacity="0.5"/>
    </svg>
    <div class="leaves" role="img" aria-label="Leaf sprig decoration" style="left:200px;top:220px;width:160px;height:90px;border-radius:50%;background:radial-gradient(ellipse,rgba(169,220,122,.6),rgba(169,220,122,0) 70%);"></div>
    <div class="brand"><span class="brand-mark"></span>Birch Hydraulic</div>
    <p class="address">4637 Heron Ridge Lane<br>Clarkston MI 48351</p>
    <dl class="contact on-green">
      <dt>Phone</dt><dd>586-555-0140</dd>
      <dt>Cell</dt><dd>586-555-0172</dd>
      <dt>Fax</dt><dd>586-555-0143</dd>
      <dt>Email</dt><dd>destry.paul@mailvane.net</dd>
    </dl>
  </section>

</main>
</body>
</html>
```